Martin Hale PA Card Logo

Current logo attached. Its 25 year old logo I have used. Looking for a new fresh elegant professional look/design for a law firm that has high net worth clientele and is estate planning business law firm. Firm mis in Palm Beach Florida.
One sided card linen stock white will be used. Logo section name section. Logo should include nice elegant design using the letter "M" perhapa (I am not wed to current font of the M on current logo.) Be creative there with logo design. My initials are MH.......color scheme I figure 3 tone... Raised Gold Foil, Blue name of firm = Martin Hale, P.A. My practice focus is Family and Business Asset Protection. My name is Martin M. Hale, Esq. Practice specialties include Asset Protection trusts, Business Succession Planning, LLC law, Estate Planning, Medicaid Planning (Maybe put those topics in bullets in a section of card. Bottom of card can be reserved smaller print address phone website and email address. Address section is not as important as logo and topics of practice on front. I foresee address section can be in dark blue. MY name and Topics dark blue as well.
Target Market(s)
affluent; business owners executives; wealth 2-10 million net worth
Industry/Entity Type
business law and estate planning
Contact Information for Business Card
White thick linen one sided

```html
<!DOCTYPE html>
<html lang="en">
<head>
<meta charset="utf-8">
<title>Martin Hale, P.A. — Business Card</title>
<link rel="stylesheet" href="https://fonts.googleapis.com/css2?family=Cinzel:wght@400&family=Cormorant+Garamond:ital,wght@0,500;1,500&display=swap">
<style>
  :root {
    --page-bg: #e9e6e1;
    --card-white: #fbfbfa;
    --navy: #0f4c8a;
    --gold: #e3ac2a;
    --text-blue: #1d4f86;
    --white: #ffffff;
  }
  * { margin: 0; padding: 0; box-sizing: border-box; }
  html, body {
    width: 1200px; height: 780px; overflow: hidden;
    background: var(--page-bg);
  }
  .canvas {
    width: 1200px; height: 780px;
    display: flex; align-items: center; justify-content: center;
  }
  .card {
    position: relative;
    width: 1000px; height: 571px;
    background: var(--card-white);
    border-radius: 26px;
    overflow: hidden;
    box-shadow: 0 10px 30px rgba(0,0,0,0.15);
  }
  .card-wave { position: absolute; inset: 0; width: 100%; height: 100%; }

  .firm-mark {
    position: absolute; left: 60px; top: 175px;
    display: flex; align-items: center; gap: 16px;
  }
  .firm-mark__dot {
    width: 22px; height: 22px; border-radius: 50%;
    background: var(--gold); flex: none;
  }
  .firm-mark__name {
    font-family: "Cinzel", serif; font-weight: 400;
    font-size: 38px; letter-spacing: 1px;
    color: var(--text-blue); white-space: nowrap;
  }
  .firm-tagline {
    position: absolute; left: 98px; top: 232px;
    font-family: "Cinzel", serif; font-size: 16px;
    letter-spacing: 2.5px; line-height: 1.5; color: var(--text-blue);
  }

  .divider {
    position: absolute; left: 462px; top: 95px;
    width: 2px; height: 230px; background: var(--gold);
  }

  .contact { position: absolute; left: 495px; top: 78px; }
  .contact__name {
    font-family: "Cinzel", serif; font-size: 30px;
    letter-spacing: 1.2px; color: var(--text-blue); line-height: 1.15;
    white-space: nowrap;
  }
  .contact__role {
    font-family: "Cormorant Garamond", serif; font-style: italic; font-weight: 500;
    font-size: 23px; color: var(--gold); margin-bottom: 10px;
  }
  .practice-list { list-style: none; }
  .practice-list__item {
    font-family: "Cormorant Garamond", serif; font-weight: 500;
    font-size: 21px; line-height: 1.3; color: var(--text-blue);
    display: flex; align-items: center; gap: 10px;
  }
  .practice-list__item::before {
    content: ""; width: 7px; height: 7px; border-radius: 50%;
    background: var(--gold); flex: none;
  }

  .card-footer {
    position: absolute; right: 60px; bottom: 28px;
    text-align: right;
    font-family: "Cormorant Garamond", serif; font-weight: 500;
    font-size: 20px; line-height: 1.35; color: var(--white);
  }
  .card-footer__line {
    display: flex; align-items: center; justify-content: flex-end; gap: 8px;
  }
  .card-footer__icon { width: 18px; height: 18px; flex: none; }
  .card-footer__gap { width: 14px; }
  .card-footer__web { font-size: 23px; letter-spacing: 0.5px; }
</style>
</head>
<body>
<main class="canvas">
  <section class="card" aria-label="Martin Hale, P.A. business card">
    <svg class="card-wave" viewBox="0 0 1000 571" preserveAspectRatio="none" aria-hidden="true">
      <path fill="var(--navy)" d="M0,505 C260,525 520,500 720,410 C840,355 910,300 1000,270 L1000,571 L0,571 Z"/>
      <path fill="var(--gold)" d="M40,492 C300,505 540,470 720,385 C830,332 900,270 985,215 C910,285 840,350 725,405 C540,488 300,512 40,492 Z"/>
    </svg>

    <div class="firm-mark">
      <span class="firm-mark__dot"></span>
      <span class="firm-mark__name">Martin Hale, P.A</span>
    </div>
    <p class="firm-tagline">FAMILY &amp; BUSINESS<br>ASSET PROTECTION</p>

    <span class="divider"></span>

    <div class="contact">
      <p class="contact__name">MARTIN M. HALE, ESQ.</p>
      <p class="contact__role">Founder/Director</p>
      <ul class="practice-list">
        <li class="practice-list__item">Asset Protection Trusts</li>
        <li class="practice-list__item">Business Succession Planning</li>
        <li class="practice-list__item">LLC Law</li>
        <li class="practice-list__item">Estate Planning</li>
        <li class="practice-list__item">Medicaid Planning</li>
      </ul>
    </div>

    <div class="card-footer">
      <p class="card-footer__line">PO BOX 456 your address, 4th street Ashford</p>
      <p class="card-footer__line">
        <svg class="card-footer__icon" viewBox="0 0 22 22" aria-hidden="true">
          <circle cx="11" cy="11" r="11" fill="var(--gold)"/>
          <rect x="7.5" y="5" width="7" height="12" rx="1.5" fill="none" stroke="#fff" stroke-width="1.6"/>
        </svg>
        (01) 5550 1234
        <span class="card-footer__gap"></span>
        <svg class="card-footer__icon" viewBox="0 0 22 22" aria-hidden="true">
          <circle cx="11" cy="11" r="11" fill="var(--gold)"/>
          <rect x="5.5" y="7" width="11" height="8" fill="none" stroke="#fff" stroke-width="1.4"/>
          <path d="M5.5,7 L11,11.5 L16.5,7" fill="none" stroke="#fff" stroke-width="1.4"/>
        </svg>
        info@halelawoffice.com
      </p>
      <p class="card-footer__line card-footer__web">www.halelawfirm.com</p>
    </div>
  </section>
</main>
</body>
</html>
```